App Design for FlavorTrek

We need an app design for a new app called FlavorTrek, which is an app designed to inspire exploration through personalized recipe generation, local restaurant discoveries, and a vibrant community platform. It caters to food enthusiasts looking to explore global cuisines or find the best local dining spots, offering a premium experience with selected features available for free.

-------UPDATED-----
This app will be AI Driven and may not be heavily dependent on media (images,videos) at first, especially for the Recipe generator feature. Our goal is to still have attractive UI. The core functionalities we are looking are the following
1. Recipe Generator: Either user choose a specific cuisine(italian,spanish), or user inputs ingredients and get recipe, or get recipe for different occasions (xmas, thanksgiving ) and get a randomly get recipe to cook, plain simple. We expect the recipes to be displayed in clear and not too generic manner starting with ingredients and expected duration at top and then step by step guide. We also intend to enable premium users to have playful action button or icon to get unlimited recipes generated until they find what they like and also have save for later feature. These premium features should be disabled for free users and prompted to subscribe if they click them with nice popup
2. Restaurant Recommendation - will have selected pictures and will be based on inputs such as zip code and other filters such as cousine types. Premium users can filter by price range, get unlimited recommendation, see actual price range in the recommendation and can save for later where they can find it later. Free users cannot filter by price (disabled) and should see it hidden in the recommendation
3. Meal Planning - will include just simple and random meal plan with just one button or limited interaction for free, users need to subscribe to get features such as customized plan such as considering allergies or diet preferences. Premium users can also get a shopping checklist of ingredients for weekly meal preps and their step by step guide for each meal recipe.
2. Community Sharing: users can view posts and engage with community content
Updates

Hello Designers,

The initial price was not fair for the work. So I have increased it. There will also be $50-100 bonus for those who come up with great designs or for those who incorporate interesting stuff. Thank you! Much appreciated 🙏

Colors
0054AA
0677BA
7BADD7
CADEEF
E8F1F8
0094D4
00A9DD
6FCCEA
C7EBF8
E9F6FB
00AB8E
00BBA5
67D7C9
C6EFE9
E9F9F6
FFC000
F8CF3A
FAE287
FDF2CF
FEFAEE
F0912C
F2A743
F7CA91
FBE8D2
FDF5EE
EE7325
F08F49
F5BC92
FAE3D3
FDF4ED
A7469A
B969AE
D3A5CF
EDDBEB
F8F0F9
6B429C
8869AF
B7A5CE
E3DAEB
F3F0F8

```html
<!DOCTYPE html>
<html lang="en">
<head>
<meta charset="utf-8">
<title>FlavorTrek – App Screens</title>
<link href="https://fonts.googleapis.com/css2?family=Poppins:wght@400;500;600;700&family=Libre+Baskerville&display=swap" rel="stylesheet">
<style>
:root{
  --board:#e9e9e9;--frame:#5a5a5a;--green:#2ec04f;--green-soft:#e6f8eb;
  --ink:#1f1f1f;--muted:#8c8c8c;--line:#ececec;--field:#f3f4f5;
  --yellow:#f8cf3a;--yellow-soft:#fdf2cf;--dark:#2b2b2b;--red:#e23b3b;--section:#b8b8b8
}
*{box-sizing:border-box;margin:0;padding:0}
body{width:905px;height:1200px;overflow:hidden;background:var(--board);font-family:Poppins,sans-serif;color:var(--ink);position:relative}
.sec{position:absolute;font-size:9px;font-weight:600;color:var(--section)}
.lbl{position:absolute;font-size:5.4px;font-weight:600;color:#2a2a2a}
.screen{position:absolute;width:80px;border:2.2px solid var(--frame);border-radius:6px;background:#fff;overflow:hidden;display:flex;flex-direction:column;padding:0 4px}
.screen.grey{background:#f6f7f8}
.sb{display:flex;justify-content:space-between;font-size:2.3px;font-weight:600;padding:3px 0 2px;position:relative;z-index:2}
.hdr{display:flex;align-items:center;gap:2px;position:relative;z-index:2;margin-bottom:2px}
.avatar{width:7px;height:7px;border-radius:50%;background:linear-gradient(135deg,#c99b84,#6e4a3c);flex:none}
.who b{display:block;font-size:2.5px;font-weight:600}
.who span{display:block;font-size:1.8px;color:var(--muted)}
.hdr .icons{margin-left:auto;display:flex;gap:2px}
.hdr .icons i{width:3.5px;height:3.5px;border:0.5px solid #777;border-radius:1px}
.on-dark,.on-dark .who span{color:#fff}
.ttl{font-size:5.6px;text-align:center;font-weight:500;margin:4px 0 3px}
.sub{font-size:2.2px;color:var(--muted);text-align:center;line-height:1.5}
.btn{height:8px;border-radius:1.5px;background:var(--green);color:#fff;font-size:2.5px;font-weight:500;display:flex;align-items:center;padding:0 3px;margin:1.5px 0;gap:2px}
.btn.center{justify-content:center}
.btn.black{background:#111}
.btn.white{background:#fff;color:var(--ink);border:0.4px solid var(--line)}
.btn.yellow{background:var(--yellow);color:#fff}
.btn.dark{background:var(--dark)}
.btn .dot{width:3px;height:3px;border-radius:50%;background:#fff;flex:none}
.btn.white .dot{background:var(--muted)}
.btn .arr{margin-left:auto}
.field{height:7px;background:var(--field);border-radius:1.5px;font-size:2.2px;color:#9a9a9a;display:flex;align-items:center;padding:0 3px;margin:1.5px 0}
.tiny{font-size:2.1px;color:var(--muted);text-align:center;margin:1.5px 0}
.tiny b{color:var(--green);font-weight:500}
.ph{border-radius:3px;flex:none}
.card{background:#fff;border-radius:2px;padding:2.5px;margin:2px 0;border:0.4px solid var(--line)}
.card h4{font-size:2.5px;font-weight:600;margin-bottom:1.5px}
.tabs{display:flex;gap:1.5px;background:var(--field);border-radius:1.5px;padding:1px;margin:1.5px 0}
.tabs span{flex:1;font-size:1.9px;text-align:center;padding:1px 0;color:var(--muted);border-radius:1px}
.tabs span.on{background:var(--yellow);color:#fff}
.input{display:flex;align-items:center;justify-content:space-between;border:0.4px solid var(--line);border-radius:1.5px;padding:1.5px 2px;font-size:2.2px;margin:1.5px 0}
.input small{display:block;font-size:1.6px;color:var(--muted)}
.add{background:var(--green);color:#fff;font-size:1.8px;padding:1px 3px;border-radius:1px}
.chips{display:grid;grid-template-columns:1fr 1fr;gap:1.5px;margin:1.5px 0}
.chips.three{grid-template-columns:1fr 1fr 1fr}
.chip{font-size:2px;border:0.4px solid #e2e2e2;border-radius:1.5px;padding:1.2px 2px;display:flex;align-items:center;gap:1.5px;justify-content:center}
.chip.lead{justify-content:flex-start}
.chip.on{border-color:var(--green);color:var(--green)}
.chip .fd{width:2.5px;height:2.5px;border-radius:50%;background:var(--red);flex:none}
.chip .fd.g{background:#6aa84f}.chip .fd.p{background:#7a3b6a}.chip .fd.b{background:#a36a2c}
.promo{display:flex;gap:2px;align-items:center;background:var(--yellow-soft);border-radius:1.5px;padding:2px;font-size:2.2px;margin:2px 0}
.promo i{width:4px;height:4px;border-radius:50%;background:var(--yellow);flex:none}
.promo small{display:block;font-size:1.6px;color:var(--muted)}
.nav{position:absolute;left:0;right:0;bottom:0;height:12px;background:#fff;border-top:0.4px solid var(--line);display:flex;justify-content:space-around;align-items:center;padding:0 3px}
.nav i{width:4px;height:4px;border:0.5px solid #9a9a9a;border-radius:1px}
.nav i.on{width:9px;height:9px;border-radius:50%;background:var(--green);border:1.5px solid #fff;margin-top:-7px}
.quick{display:flex;justify-content:space-around;margin-top:4px}
.quick div{display:flex;flex-direction:column;align-items:center;gap:1.5px;font-size:1.9px;color:var(--green)}
.quick i{width:12px;height:12px;border-radius:50%;border:0.5px solid var(--line);display:flex;align-items:center;justify-content:center}
.quick i::after{content:"";width:6px;height:5px;border:0.6px solid var(--green);border-radius:1px}
.quick.sq i{border-radius:2px}
.step{display:flex;gap:2px;font-size:1.9px;color:#666;line-height:1.5;margin:1.5px 0}
.step::before{content:"";width:2.5px;height:2.5px;border-radius:50%;background:var(--green);flex:none;margin-top:0.6px}
.sect{font-size:2.3px;font-weight:600;margin:2px 0 1px}
.row2{display:flex;gap:2px}.row2>*{flex:1}
.tile{height:19px;border-radius:2px;background:linear-gradient(135deg,#3a2e22,#6b4b2a);color:#fff;font-size:1.7px;display:flex;align-items:flex-end;justify-content:center;padding-bottom:1px}
.grid3{display:grid;grid-template-columns:repeat(3,1fr);gap:2px;margin:1.5px 0}
.bg-photo{position:absolute;left:0;right:0;top:0}
.serif{font-family:"Libre Baskerville",serif}
.filters{display:grid;grid-template-columns:1fr 1fr 1fr;gap:1px;font-size:1.6px;color:#ddd;margin-top:2px}
.fbox{display:flex;gap:1px}
.fbox span{flex:1;background:#fff;border-radius:1px;font-size:1.7px;color:var(--ink);text-align:center;padding:1px 0}
.fbox span.y{background:var(--yellow);color:#fff}
.daybar{display:flex;justify-content:space-between;font-size:2.2px;padding:2px 1px;border-bottom:0.4px solid var(--line)}
.days{display:flex;justify-content:space-between;margin:2px 0}
.days i{width:4.5px;height:4.5px;border-radius:50%;border:0.4px solid #ccc;font-style:normal;font-size:1.5px;display:flex;align-items:center;justify-content:center;color:var(--muted)}
.days i.on{background:var(--green);color:#fff;border-color:var(--green)}
.meal{display:flex;gap:2px;align-items:center;border:0.4px solid var(--line);border-radius:1.5px;padding:2px;margin:2px 0;font-size:2.1px;font-weight:500}
.meal small{display:block;font-size:1.6px;color:var(--muted);font-weight:400}
.meal .ph{width:11px;height:11px;border-radius:1.5px;background:linear-gradient(135deg,#c7a26f,#7a4b2a)}
.meal .edit{margin-left:auto;width:3.5px;height:3.5px;border-radius:50%;border:0.4px solid #bbb;flex:none}
.item{display:flex;gap:2.5px;align-items:center;background:#fff;border-radius:1.5px;padding:2px;margin:2px 0;font-size:2.1px}
.item small{display:block;font-size:1.6px;color:var(--muted)}
.item i{width:4px;height:4px;border-radius:50%;background:var(--red);flex:none}
.rest .ph{height:25px;background:linear-gradient(135deg,#6b3f22,#c98a4a 55%,#3a2518)}
.rest b{display:block;font-size:2.2px;font-weight:600;margin-top:1.5px}
.rest p{font-size:1.6px;color:var(--muted)}
.rest .meta{display:flex;justify-content:space-between;font-size:1.6px;color:var(--muted);margin:1px 0 3px}
.saved{display:grid;grid-template-columns:1fr 1fr;gap:3px;margin-top:2px}
.saved div{font-size:1.9px;font-weight:500}
.saved .ph{height:22px;background:linear-gradient(135deg,#c4562b,#e9a25a 60%,#6a8a3a)}
.saved small{display:block;font-size:1.5px;color:var(--muted);font-weight:400}
.dim{position:absolute;inset:0;background:rgba(40,40,40,.55);z-index:3}
.popup{position:absolute;left:4px;right:4px;top:45px;background:#fff;border-radius:2px;z-index:4;padding:3px}
.note{position:absolute;font-size:4.2px;color:#333;display:flex;align-items:center;gap:4px}
.note::before{content:"";width:14px;height:0.5px;background:#777}
</style>
</head>
<body>

<!-- Basic screens -->
<div class="sec" style="left:56px;top:10px">Basic Screen</div>

<div class="lbl" style="left:58px;top:25px">00.Login screen</div>
<div class="screen" style="left:58px;top:36px;height:169px">
  <div class="sb"><span>5:50 am</span><span>•••</span></div>
  <div class="ph" role="img" aria-label="Bowl of fresh salad with shrimp and avocado" style="height:78px;margin:0 -4px;border-radius:0;background:radial-gradient(circle at 55% 40%,#9fcf6a,#e8c07a 45%,#f3efe8 75%)"></div>
  <div class="sub" style="margin:5px 0 3px">Hi, Please sign up to access your account</div>
  <div class="btn black"><span class="dot"></span>Orchard sign in</div>
  <div class="btn white"><span class="dot"></span>Continue with Glimmer</div>
  <div class="btn"><span class="dot"></span>Sign up with Email</div>
  <div class="tiny">Already have an account? <span style="color:var(--ink)">Log in</span></div>
</div>

<div class="lbl" style="left:151px;top:25px">01.Login screen-1</div>
<div class="screen" style="left:151px;top:36px;height:169px">
  <div class="sb"><span>5:50 am</span><span>•••</span></div>
  <div class="ph" role="img" aria-label="Cooking pot illustration with vegetables" style="width:34px;height:30px;margin:30px auto 6px;border-radius:50%;background:radial-gradient(circle,#8a8f99,#c9e6d4 70%,#fff)"></div>
  <div class="sub" style="margin-bottom:3px">Hi, Please sign up to access your account</div>
  <div class="btn black"><span class="dot"></span>Orchard sign in</div>
  <div class="btn white"><span class="dot"></span>Continue with Glimmer</div>
  <div class="btn"><span class="dot"></span>Sign up with Email</div>
  <div class="tiny">Already have an account? <span style="color:var(--ink)">Log in</span></div>
</div>

<div class="lbl" style="left:244px;top:25px">02.Login screen-2</div>
<div class="screen" style="left:244px;top:36px;height:169px">
  <div class="sb"><span>5:50 am</span><span>•••</span></div>
  <div class="ph" role="img" aria-label="Cooking pot illustration with vegetables" style="width:30px;height:26px;margin:6px auto 4px;border-radius:50%;background:radial-gradient(circle,#8a8f99,#c9e6d4 70%,#fff)"></div>
  <div class="ttl" style="font-size:4.4px;margin:2px 0 1px">Welcome to <b>FlavorTrek</b></div>
  <div class="sub" style="margin-bottom:4px">Please enter the details below to continue</div>
  <div class="field">Email Address</div>
  <div class="field">Password</div>
  <div class="tiny" style="text-align:right">Reset Password?</div>
  <div class="btn">Login<span class="arr">→</span></div>
  <div class="tiny">Don't have account? <b>Create an Account</b></div>
  <div class="tiny" style="margin:4px 0">— or continue with —</div>
  <div class="row2"><div class="btn black center">Orchard</div><div class="btn white center">Glimmer</div></div>
</div>

<div class="lbl" style="left:337px;top:25px">03.Register screen</div>
<div class="screen" style="left:337px;top:36px;height:169px">
  <div class="sb"><span>5:50 am</span><span>•••</span></div>
  <div style="font-size:3px;text-align:center;margin:2px 0 6px">Register</div>
  <div class="ttl" style="font-size:4.2px;margin:0">Create a <b>New Account</b></div>
  <div class="sub" style="margin-bottom:3px">Enter your information's below</div>
  <div class="field">First Name</div>
  <div class="field">Last Name</div>
  <div class="field">Email Address</div>
  <div class="field">Password</div>
  <div class="field">Retype Password</div>
  <div class="btn" style="margin-top:3px">Register<span class="arr">→</span></div>
  <div class="tiny">Already have an account? <b>Sign in</b></div>
</div>

<div class="lbl" style="left:430px;top:25px">04.Forgot password</div>
<div class="screen" style="left:430px;top:36px;height:164px">
  <div class="sb"><span>5:50 am</span><span>•••</span></div>
  <div style="font-size:3px;text-align:center;margin:2px 0 6px">Forgot Password</div>
  <div class="ttl" style="font-size:4.2px;margin:0">Forgot your <b>Password?</b></div>
  <div class="sub" style="margin-bottom:3px">Enter the email address associated with your account</div>
  <div class="field">jordan@mailnest.com</div>
  <div class="btn">Send Code<span class="arr">→</span></div>
</div>

<div class="lbl" style="left:519px;top:25px">05.Set new password</div>
<div class="screen" style="left:519px;top:36px;height:164px">
  <div class="sb"><span>5:50 am</span><span>•••</span></div>
  <div style="font-size:3px;text-align:center;margin:2px 0 6px">Reset Password</div>
  <div class="ttl" style="font-size:4.2px;margin:0">Set New <b>Password</b></div>
  <div class="sub" style="margin-bottom:3px">Please enter your new password and continue use the account</div>
  <div class="field">Password</div>
  <div class="field">Retype Password</div>
  <div class="btn">Save<span class="arr">→</span></div>
  <div class="tiny" style="color:var(--green);text-align:left">✓ Password Changed Successfully – <span style="color:var(--ink)">Home</span></div>
</div>

<!-- Home screens -->
<div class="sec" style="left:56px;top:241px">Home Screen</div>

<div class="lbl" style="left:58px;top:275px">06.Home one</div>
<div class="screen" style="left:58px;top:288px;height:169px">
  <div class="sb"><span>5:50 am</span><span>•••</span></div>
  <div class="hdr"><span class="avatar"></span><div class="who"><b>Hello Mira</b><span>Maple Court, Lakeview</span></div></div>
  <div class="ttl" style="margin-top:26px;margin-bottom:0">Hi User,</div>
  <div class="sub" style="font-size:3.2px;color:var(--ink);margin-bottom:4px">What's What'd you like today?</div>
  <div class="btn"><span class="dot"></span>Get a Recipe<span class="arr">»</span></div>
  <div class="tiny" style="text-align:left">Discover recipes based on ingredients, cuisines or generate a random recipe.</div>
  <div class="quick"><div><i></i>Eat Out</div><div><i></i>Plan a Meal</div><div><i></i>Community</div></div>
</div>

<div class="lbl" style="left:151px;top:275px">07.Home two</div>
<div class="screen" style="left:151px;top:288px;height:169px">
  <div class="sb"><span>5:50 am</span><span>•••</span></div>
  <div class="hdr"><span class="avatar"></span><div class="who"><b>Hello Mira</b><span>Maple Court, Lakeview</span></div></div>
  <div class="ttl" style="margin-top:26px;margin-bottom:0">Hi User,</div>
  <div class="sub" style="font-size:3.2px;color:var(--ink);margin-bottom:4px">What's What'd you like today?</div>
  <div class="btn center">Get a Recipe</div>
  <div class="tiny" style="text-align:left">Discover recipes based on ingredients, cuisines or generate a random recipe.</div>
  <div class="quick sq"><div><i></i>Eat Out</div><div><i></i>Plan a Meal</div><div><i></i>Community</div></div>
</div>

<div class="lbl" style="left:246px;top:275px">08.Home three</div>
<div class="screen" style="left:246px;top:288px;height:173px">
  <div class="ph bg-photo" role="img" aria-label="Bowl of chickpea curry with spices on a white table" style="height:88px;border-radius:0;background:radial-gradient(circle at 50% 55%,#d9542b,#e99a5a 35%,#f1ede8 65%)"></div>
  <div class="sb"><span>5:50 am</span><span>•••</span></div>
  <div class="hdr"><span class="avatar"></span><div class="who"><b>Hello Mira</b><span>Maple Court, Lakeview</span></div></div>
  <div class="ttl" style="margin-top:70px;margin-bottom:0">Hi User,</div>
  <div class="sub" style="font-size:3.2px;color:var(--ink);margin-bottom:3px">What's What'd you like today?</div>
  <div class="btn" style="border-radius:4px"><span class="dot"></span>Get a Recipe<span class="arr">»</span></div>
  <div class="tiny" style="text-align:left">Discover recipes based on ingredients, cuisines or generate a random recipe.</div>
  <div class="quick"><div><i></i>Eat Out</div><div><i></i>Plan a Meal</div><div><i></i>Community</div></div>
</div>

<div class="lbl" style="left:345px;top:275px">09.Home four</div>
<div class="screen" style="left:345px;top:288px;height:169px;background:#1e1e1e">
  <div class="ph bg-photo" role="img" aria-label="Overhead spread of dark dishes, curries and grains" style="height:169px;border-radius:0;background:radial-gradient(circle at 30% 20%,#8a5a2a,transparent 30%),radial-gradient(circle at 70% 45%,#b5762e,transparent 30%),radial-gradient(circle at 35% 65%,#5a7a2a,transparent 25%),#1f1f1f"></div>
  <div class="sb on-dark"><span>5:50 am</span><span>•••</span></div>
  <div class="hdr on-dark" style="margin-top:90px"><span class="avatar"></span><div class="who"><b>Hello Mira</b><span>Maple Court, Lakeview</span></div></div>
  <div class="btn" style="border-radius:4px;position:relative"><span class="dot"></span>Get a Recipe<span class="arr">»</span></div>
  <div class="tiny" style="text-align:left;color:#ccc;position:relative">Discover recipes based on ingredients, cuisines or generate a random recipe.</div>
  <div class="quick" style="position:relative"><div><i style="background:#fff"></i>Eat Out</div><div><i style="background:#fff"></i>Plan a Meal</div><div><i style="background:#fff"></i>Community</div></div>
</div>

<!-- Recipe -->
<div class="sec" style="left:470px;top:245px">Recipe</div>

<div class="lbl" style="left:468px;top:271px">10.Recipe one</div>
<div class="screen grey" style="left:468px;top:283px;height:185px">
  <div class="sb"><span>5:50 am</span><span>•••</span></div>
  <div class="hdr"><span class="avatar"></span><div class="who"><b>Hello Mira</b><span>Maple Court, Lakeview</span></div><div class="icons"><i></i></div></div>
  <div class="ttl">Recipes</div>
  <div class="btn"><span class="dot"></span>Surprise Me<span class="arr">»</span></div>
  <div class="card">
    <h4 style="text-align:center">Customise Your Recipe</h4>
    <div class="tabs"><span class="on">Add Ingredients</span><span>Cuisine</span><span>Occasion</span></div>
    <div class="input"><div><small>Add your ingredients</small>Tomato</div><span class="add">ADD</span></div>
    <div class="chips"><div class="chip lead"><i class="fd"></i>Tomato</div><div class="chip lead"><i class="fd"></i>Beef</div><div class="chip lead"><i class="fd p"></i>Onion</div><div class="chip lead"><i class="fd g"></i>Avocado</div></div>
    <div class="promo"><i></i><div>Subscribe to<small>Add Maximum Cooking Time</small></div></div>
    <div class="btn center">Get Your Recipe</div>
  </div>
  <div class="nav"><i></i><i class="on"></i><i></i><i></i><i></i></div>
</div>

<div class="lbl" style="left:563px;top:271px">11.Recipe two</div>
<div class="screen grey" style="left:563px;top:283px;height:199px">
  <div class="sb"><span>5:50 am</span><span>•••</span></div>
  <div class="hdr"><span class="avatar"></span><div class="who"><b>Hello Mira</b><span>Maple Court, Lakeview</span></div><div class="icons"><i></i></div></div>
  <div class="ttl">Recipes</div>
  <div class="ph" role="img" aria-label="Surprise me banner with a bowl of curry" style="height:32px;background:linear-gradient(90deg,#2a2a2a 40%,#e0a040)"></div>
  <div class="card" style="margin-top:4px">
    <h4 style="text-align:center">Customise Your Recipe</h4>
    <div class="tabs"><span class="on">Add Ingredients</span><span>Cuisine</span><span>Occasion</span></div>
    <div class="input"><div><small>Add your ingredients</small>Tomato</div><span class="add">ADD</span></div>
    <div class="chips"><div class="chip lead"><i class="fd"></i>Tomato</div><div class="chip lead"><i class="fd"></i>Beef</div><div class="chip lead"><i class="fd p"></i>Onion</div><div class="chip lead"><i class="fd g"></i>Avocado</div></div>
    <div class="promo"><i></i><div>Subscribe to<small>Add Maximum Cooking Time</small></div></div>
    <div class="btn center">Get Your Recipe</div>
  </div>
  <div class="nav"><i></i><i class="on"></i><i></i><i></i><i></i></div>
</div>

<!-- Cuisine -->
<div class="sec" style="left:687px;top:245px">Cuisine</div>

<div class="lbl" style="left:686px;top:268px">12.Cuisine one</div>
<div class="screen grey" style="left:686px;top:281px;height:210px">
  <div class="sb"><span>5:50 am</span><span>•••</span></div>
  <div class="hdr"><span class="avatar"></span><div class="who"><b>Hello Mira</b><span>Maple Court, Lakeview</span></div><div class="icons"><i></i></div></div>
  <div class="ttl">Recipes</div>
  <div class="btn"><span class="dot"></span>Surprise Me<span class="arr">»</span></div>
  <div class="card">
    <h4 style="text-align:center">Customise Your Recipe</h4>
    <div class="tabs"><span>Add Ingredients</span><span class="on">Cuisine</span><span>Occasion</span></div>
    <div style="display:flex;justify-content:space-between;align-items:center;font-size:2px;margin:2px 0">Choose Your Cuisine<span class="promo" style="margin:0;padding:1px 2px;font-size:1.7px">Subscribe to</span></div>
    <div class="chips three"><div class="chip on">American</div><div class="chip on">Indian</div><div class="chip">Mexican</div><div class="chip">Japanese</div><div class="chip">Chinese</div><div class="chip">Italian</div><div class="chip">African</div><div class="chip">French</div><div class="chip">Spanish</div></div>
  </div>
  <div class="card">
    <div class="input"><div><small>Avoid ingredients</small>Tomato</div><span class="add">ADD</span></div>
    <div class="chips"><div class="chip lead"><i class="fd"></i>Tomato</div><div class="chip lead"><i class="fd"></i>Beef</div></div>
    <div class="btn center">Get Your Recipe</div>
  </div>
  <div class="nav"><i></i><i class="on"></i><i></i><i></i><i></i></div>
</div>

<div class="lbl" style="left:781px;top:268px">12.Cuisine two</div>
<div class="screen grey" style="left:781px;top:281px;height:242px">
  <div class="sb"><span>5:50 am</span><span>•••</span></div>
  <div class="hdr"><span class="avatar"></span><div class="who"><b>Hello Mira</b><span>Maple Court, Lakeview</span></div><div class="icons"><i></i></div></div>
  <div class="ttl">Recipes</div>
  <div class="ph" role="img" aria-label="Surprise me banner with a bowl of soup" style="height:32px;background:linear-gradient(90deg,#f5f5f5 40%,#d9542b)"></div>
  <div class="card" style="margin-top:4px">
    <h4 style="text-align:center">Customise Your Recipe</h4>
    <div class="tabs"><span>Add Ingredients</span><span class="on">Cuisine</span><span>Occasion</span></div>
    <div style="display:flex;justify-content:space-between;align-items:center;font-size:2px;margin:2px 0">Choose Your Cuisine<span class="promo" style="margin:0;padding:1px 2px;font-size:1.7px">Subscribe to</span></div>
    <div class="grid3">
      <div class="tile" role="img" aria-label="African cuisine region tile">African</div>
      <div class="tile" role="img" aria-label="Indian cuisine region tile">Indian</div>
      <div class="tile" role="img" aria-label="Australian cuisine region tile">Australian</div>
      <div class="tile" role="img" aria-label="Italian cuisine region tile">Italian</div>
      <div class="tile" role="img" aria-label="Spanish cuisine region tile">Spanish</div>
      <div class="tile" role="img" aria-label="American cuisine region tile">American</div>
    </div>
  </div>
  <div class="card">
    <div class="input"><div><small>Avoid ingredients</small>Tomato</div><span class="add">ADD</span></div>
    <div class="chips"><div class="chip lead"><i class="fd"></i>Tomato</div><div class="chip lead"><i class="fd"></i>Beef</div></div>
    <div class="btn center">Get Your Recipe</div>
  </div>
  <div class="nav"><i></i><i class="on"></i><i></i><i></i><i></i></div>
</div>

<!-- Recipe details -->
<div class="sec" style="left:53px;top:506px">Recipe Details</div>

<div class="lbl" style="left:54px;top:527px">13.Recipe Details</div>
<div class="screen grey" style="left:54px;top:542px;height:277px">
  <div class="sb"><span>5:50 am</span><span>•••</span></div>
  <div class="hdr"><span class="avatar"></span><div class="who"><b>Hello Mira</b><span>Maple Court, Lakeview</span></div><div class="icons"><i></i></div></div>
  <div class="ttl">Recipe Details</div>
  <div class="btn"><span class="dot"></span>Surprise Me<span class="arr">»</span></div>
  <div class="card">
    <h4>Customise Your Recipe</h4>
    <div class="tiny" style="text-align:left">Choose Cuisine</div>
    <div style="display:flex;gap:1.5px"><span class="chip">American</span><span class="chip">Indian</span><span class="chip" style="background:var(--green);color:#fff;border:none">Load More</span></div>
  </div>
  <div class="card">
    <h4>Gongura Chicken Curry Recipe</h4>
    <div class="tiny" style="text-align:left">⏱ Eat Cooking Time : 20min</div>
    <div class="sect">Ingredients</div>
    <div class="chips"><div class="chip lead"><i class="fd"></i>Tomato</div><div class="chip lead"><i class="fd"></i>Beef</div></div>
    <div class="sect">Spices</div>
    <div class="chips"><div class="chip lead"><i class="fd b"></i>Cardamom</div><div class="chip lead"><i class="fd b"></i>Cinnamon</div></div>
  </div>
  <div class="card">
    <div class="sect">Preparation</div>
    <div class="step">Start by washing the gongura leaves nicely. Transfer them to a pan and cook with green chillies, salt, and a bit of water for about 4 to 5 minutes.</div>
    <div class="step">Allow it to cool, then grind them to a smooth paste. Now, heat some oil in a kadhai set on a low-medium flame.</div>
    <div class="step">Add chopped onions and saute until golden brown in colour. Add haldi, coriander powder, jeera, and ginger-garlic paste and fry for a few seconds.</div>
    <div class="step">You can add some more water at this stage if needed. Once done, add the prepared gongura paste and let it simmer again for a minute or two.</div>
    <div class="row2"><div class="btn dark center">Get New</div><div class="btn center">Save For Later</div></div>
  </div>
</div>

<div class="lbl" style="left:161px;top:527px">14.Cuisine Popup</div>
<div class="screen grey" style="left:161px;top:542px;height:163px">
  <div class="sb"><span>5:50 am</span><span>•••</span></div>
  <div class="hdr"><span class="avatar"></span><div class="who"><b>Hello Mira</b><span>Maple Court, Lakeview</span></div><div class="icons"><i></i></div></div>
  <div class="ttl">Recipe Details</div>
  <div class="btn"><span class="dot"></span>Surprise Me</div>
  <div style="height:80px"></div>
  <div class="sect">Spices</div>
  <div class="chips"><div class="chip lead"><i class="fd b"></i>Cardamom</div><div class="chip lead"><i class="fd b"></i>Cinnamon</div></div>
  <div class="sect">Preparation</div>
  <div class="dim"></div>
  <div class="popup">
    <h4 style="font-size:2.5px;font-weight:600;margin-bottom:2px">Add Your Cuisine</h4>
    <div class="chips three"><div class="chip on">American</div><div class="chip on">Indian</div><div class="chip">Mexican</div><div class="chip">Japanese</div><div class="chip">Chinese</div><div class="chip">Italian</div><div class="chip">African</div><div class="chip">French</div><div class="chip">Spanish</div></div>
    <div class="btn center" style="margin-top:3px">Load Cuisine</div>
  </div>
</div>

<!-- Place to eat -->
<div class="sec" style="left:268px;top:503px">Place to eat</div>

<div class="lbl" style="left:269px;top:527px">15.Place to eat</div>
<div class="screen" style="left:269px;top:542px;height:220px">
  <div class="ph bg-photo" role="img" aria-label="Dark restaurant interior backdrop" style="height:87px;border-radius:0;background:linear-gradient(180deg,#1d1d1d,#3b3b3b)"></div>
  <div class="sb on-dark"><span>5:50 am</span><span>•••</span></div>
  <div class="hdr on-dark"><span class="avatar"></span><div class="who"><b>Hello Mira</b><span>Maple Court, Lakeview</span></div><div class="icons"><i style="background:#fff;border-radius:50%"></i></div></div>
  <div class="serif" style="position:relative;color:#fff;font-size:4px;text-align:center;margin:5px 0 3px">Lets get you a place to eat</div>
  <div style="position:relative;background:#fff;border-radius:1.5px;font-size:2.3px;width:34px;margin:0 auto;padding:1px 2px;text-align:center">Zip Code 123456</div>
  <div class="filters" style="position:relative;margin-top:12px"><span>Choose Meal Type</span><span>Distance</span><span>Price Range</span></div>
  <div class="fbox" style="position:relative"><span class="y">Cuisine</span><span>Occasion</span><span>5M</span><span>50</span><span>2500</span></div>
  <div class="sub" style="margin:9px 0 4px;font-size:2.4px">Here's a good restaurant based on your preferences. A very nice food here.</div>
  <div class="rest"><div class="ph" role="img" aria-label="Warmly lit restaurant dining room" style="height:42px"></div>
    <b class="serif" style="font-weight:400">The Copper Clove</b><p>⌖ 4410 Birchway Lane, MN 55012</p></div>
  <div class="row2" style="margin-top:5px"><div class="btn yellow center">Premium</div><div class="btn center">Save for Later</div></div>
</div>

<div class="lbl" style="left:367px;top:527px">16.Place to eat – subscription</div>
<div class="screen" style="left:367px;top:542px;height:215px">
  <div class="ph bg-photo" role="img" aria-label="Dark restaurant interior backdrop" style="height:87px;border-radius:0;background:linear-gradient(180deg,#1d1d1d,#3b3b3b)"></div>
  <div class="sb on-dark"><span>5:50 am</span><span>•••</span></div>
  <div class="hdr on-dark"><span class="avatar"></span><div class="who"><b>Hello Mira</b><span>Maple Court, Lakeview</span></div><div class="icons"><i style="background:#fff;border-radius:50%"></i></div></div>
  <div class="serif" style="position:relative;color:#fff;font-size:4px;text-align:center;margin:5px 0 3px">Lets get you a place to eat</div>
  <div style="position:relative;background:#fff;border-radius:1.5px;font-size:2.3px;width:34px;margin:0 auto;padding:1px 2px;text-align:center">Zip Code 123456</div>
  <div style="position:relative;align-self:flex-end;background:#eee;border-radius:3px;font-size:1.9px;padding:1px 3px;margin-top:5px">● Subscribe to Add</div>
  <div class="filters" style="position:relative;margin-top:1px"><span>Choose Meal Type</span><span>Distance</span><span>Price Range</span></div>
  <div class="fbox" style="position:relative"><span class="y">Cuisine</span><span>Occasion</span><span>5M</span><span>50</span><span>2500</span></div>
  <div class="sub" style="margin:7px 0 4px;font-size:2.4px">Here's a good restaurant based on your preferences. A very nice food here.</div>
  <div class="rest"><div class="ph" role="img" aria-label="Warmly lit restaurant dining room" style="height:42px"></div>
    <b class="serif" style="font-weight:400">The Copper Clove</b><p>⌖ 4410 Birchway Lane, MN 55012</p></div>
  <div class="row2" style="margin-top:5px"><div class="btn yellow center">Premium</div><div class="btn center">Save for Later</div></div>
</div>

<!-- Meal prep -->
<div class="lbl" style="left:491px;top:527px">17.Meal Prep</div>
<div class="screen grey" style="left:491px;top:542px;height:357px">
  <div class="ph bg-photo" role="img" aria-label="Dark food spread backdrop" style="height:62px;border-radius:0;background:linear-gradient(180deg,#2a2622,#4a3a2a)"></div>
  <div class="sb on-dark"><span>5:50 am</span><span>•••</span></div>
  <div class="hdr on-dark"><span class="avatar"></span><div class="who"><b>Hello Mira</b><span>Maple Court, Lakeview</span></div><div class="icons"><i style="background:#fff;border-radius:50%"></i></div></div>
  <div class="serif" style="position:relative;color:#fff;font-size:4px;text-align:center;margin:8px 0 4px">Choose Meal Prep Duration</div>
  <div style="position:relative;display:flex;justify-content:center;gap:3px;font-size:2.2px"><span style="background:#fff;padding:1px 3px;border-radius:1px">2 Days</span><span style="background:#fff;padding:1px 3px;border-radius:1px;border:0.5px solid var(--yellow)">3 Days</span><span style="background:#fff;padding:1px 3px;border-radius:1px">5 Days</span></div>
  <div class="btn" style="margin-top:11px">Day 1<span class="arr">⌄</span></div>
  <div class="card">
    <div class="tabs" style="background:none"><span class="on">I have Ingredients</span><span>Generate Ingredients</span></div>
    <div class="input"><div><small>Add Your Ingredients</small>Tomato</div><span class="add">ADD</span></div>
    <div class="chips"><div class="chip lead"><i class="fd"></i>Tomato</div><div class="chip lead"><i class="fd"></i>Beef</div></div>
    <h4 style="margin-top:2px">Gongura Chicken Curry Recipe</h4>
    <div class="tiny" style="text-align:left">⏱ Eat Cooking Time : 20min</div>
    <div class="sect">Ingredients</div>
    <div class="chips"><div class="chip lead"><i class="fd"></i>Tomato</div><div class="chip lead"><i class="fd"></i>Beef</div></div>
    <div class="sect">Spices</div>
    <div class="chips"><div class="chip lead"><i class="fd b"></i>Cardamom</div><div class="chip lead"><i class="fd b"></i>Cinnamon</div></div>
    <div class="sect">Preparation</div>
    <div class="step">Start by washing the gongura leaves nicely. Transfer them to a pan and cook with green chillies, salt, and a bit of water for about 4 to 5 minutes.</div>
    <div class="step">Allow it to cool, then grind them to a smooth paste. Now, heat some oil in a kadhai set on a low-medium flame.</div>
    <div class="step">Add chopped onions and saute until golden brown in colour. Add haldi, coriander powder, jeera, and ginger-garlic paste and fry for a few seconds.</div>
    <div class="step">You can add some more water at this stage if needed. Once done, add the prepared gongura paste and let it simmer again for a minute or two.</div>
    <div class="btn yellow">Save Ingredients<span class="arr">▣</span></div>
  </div>
  <div class="daybar"><span>Day 2</span><span>⌄</span></div>
  <div class="daybar"><span>Day 3</span><span>⌄</span></div>
  <div class="daybar"><span>Day 4</span><span>⌄</span></div>
  <div class="row2" style="margin-top:6px"><div class="btn dark center">Get New</div><div class="btn center">Save For Later</div></div>
</div>

<!-- Row 4 -->
<div class="lbl" style="left:52px;top:875px">18.Saved Restaurant</div>
<div class="screen grey" style="left:54px;top:888px;height:222px">
  <div class="sb"><span>5:50 am</span><span>•••</span></div>
  <div class="hdr"><span class="avatar"></span><div class="who"><b>Hello Mira</b><span>Maple Court, Lakeview</span></div><div class="icons"><i></i><i></i></div></div>
  <div class="ttl">Saved Restaurant</div>
  <div class="rest"><div class="ph" role="img" aria-label="Restaurant lounge with fireplace"></div><b>The Lumen Hall</b><p>This is the best Sunday chilli beef, bacon, tomatoes, chopped veggies...</p><div class="meta"><span>★ 4.8 (120 Ratings)</span><span>5.5mi</span><span style="color:var(--green)">Opened</span></div></div>
  <div class="rest"><div class="ph" role="img" aria-label="Bright restaurant dining hall" style="background:linear-gradient(135deg,#8a6a4a,#d9c2a0 60%,#5a3e2a)"></div><b>The Lumen Hall</b><p>This is the best Sunday chilli beef, bacon, tomatoes, chopped veggies...</p><div class="meta"><span>★ 4.8 (120 Ratings)</span><span>5.5mi</span><span style="color:var(--green)">Opened</span></div></div>
  <div class="rest"><div class="ph" role="img" aria-label="Hotel restaurant with red lighting" style="background:linear-gradient(135deg,#5a1e14,#b5452a 60%,#2a1410)"></div><b>Willow Garden Inn</b><p>This is the best Sunday chilli beef, bacon, tomatoes, chopped veggies...</p></div>
  <div class="nav"><i></i><i class="on"></i><i></i><i></i><i></i></div>
</div>

<div class="lbl" style="left:157px;top:875px">19.Saved Recipes</div>
<div class="screen" style="left:154px;top:888px;height:201px">
  <div class="sb"><span>5:50 am</span><span>•••</span></div>
  <div class="hdr"><span class="avatar"></span><div class="who"><b>Hello Mira</b><span>Maple Court, Lakeview</span></div><div class="icons"><i></i><i></i></div></div>
  <div class="ttl">Saved Recipes</div>
  <div class="saved">
    <div><div class="ph" role="img" aria-label="Asparagus frittata dish"></div>Asparagus Frittata<small>⏱ 20min</small></div>
    <div><div class="ph" role="img" aria-label="Baked salmon with vegetables"></div>Backed Salmon<small>⏱ 20min</small></div>
    <div><div class="ph" role="img" aria-label="Roasted eggplant salad"></div>Roasted eggplant salad<small>⏱ 20min</small></div>
    <div><div class="ph" role="img" aria-label="Pozole bowl"></div>Appetizing pozole bowl<small>⏱ 20min</small></div>
    <div><div class="ph" role="img" aria-label="Asparagus frittata dish"></div>Asparagus Frittata<small>⏱ 20min</small></div>
    <div><div class="ph" role="img" aria-label="Baked salmon bowl"></div>Backed Salmon<small>⏱ 20min</small></div>
  </div>
  <div class="nav"><i></i><i class="on"></i><i></i><i></i><i></i></div>
</div>

<div class="lbl" style="left:247px;top:875px">20.Shop Ingredient</div>
<div class="screen grey" style="left:247px;top:888px;height:184px">
  <div class="sb"><span>5:50 am</span><span>•••</span></div>
  <div class="hdr"><span class="avatar"></span><div class="who"><b>Hello Mira</b><span>Maple Court, Lakeview</span></div><div class="icons"><i></i><i></i></div></div>
  <div class="ttl">Shop Ingredient</div>
  <div class="btn"><span class="dot"></span>Add Your Own Ingredient</div>
  <div class="item" style="margin-top:4px"><i style="background:#e6c08a"></i><div>Eggs<small>as needed</small></div></div>
  <div class="item"><i style="background:#f3d54a"></i><div>Lemon<small>as needed</small></div></div>
  <div class="item"><i></i><div>Tomato<small>2 piece</small></div></div>
  <div class="item"><i></i><div>Tomato<small>2 piece</small></div></div>
  <div class="item"><i style="background:#8aa84f"></i><div>Cardamom<small>2 piece</small></div></div>
  <div class="nav"><i></i><i class="on"></i><i></i><i></i><i></i></div>
</div>

<div class="lbl" style="left:344px;top:875px">21.Meal Plan</div>
<div class="screen" style="left:340px;top:888px;height:185px">
  <div class="sb"><span>5:50 am</span><span>•••</span></div>
  <div class="hdr"><span class="avatar"></span><div class="who"><b>Hello Mira</b><span>Maple Court, Lakeview</span></div><div class="icons"><i></i><i></i></div></div>
  <div class="ttl">Meal Plan</div>
  <div class="tiny">Ready to plan this week</div>
  <div class="days"><i>16</i><i>17</i><i>18</i><i class="on">19</i><i>20</i><i>21</i><i>22</i></div>
  <div class="promo"><i></i><div>Subscribe to<small>Add your allergies or diet preferences</small></div></div>
  <div class="meal"><span class="ph" role="img" aria-label="Scrambled eggs with spinach and pita"></span><div><small>Morning</small>Scrambled Eggs with Spinach, Feta &amp; Pita</div></div>
  <div class="meal"><span class="ph" role="img" aria-label="Black bean salad"></span><div><small>Afternoon</small>No-Cook Black Bean Salad</div></div>
  <div class="meal"><span class="ph" role="img" aria-label="Glazed salmon with garlic spinach"></span><div><small>Evening</small>Gochujang-Glazed Salmon with Garlic Spinach</div></div>
  <div class="nav"><i></i><i class="on"></i><i></i><i></i><i></i></div>
</div>

<div class="lbl" style="left:437px;top:912px">22.Meal Plan – Subscription</div>
<div class="screen" style="left:437px;top:926px;height:186px">
  <div class="sb"><span>5:50 am</span><span>•••</span></div>
  <div class="hdr"><span class="avatar"></span><div class="who"><b>Hello Mira</b><span>Maple Court, Lakeview</span></div><div class="icons"><i></i><i></i></div></div>
  <div class="ttl">Meal Plan</div>
  <div class="tiny">Ready to plan this week</div>
  <div class="days"><i>16</i><i>17</i><i>18</i><i class="on">19</i><i>20</i><i>21</i><i>22</i></div>
  <div class="promo" style="background:var(--green-soft)"><i style="background:var(--green)"></i><div>Vegetarian <span style="background:var(--green);color:#fff;border-radius:2px;padding:0 1.5px;font-size:1.6px">Diet Plan</span><small>Excludes: Red Meat, Poultry, Fish, Shellfish</small></div></div>
  <div class="meal"><span class="ph" role="img" aria-label="Scrambled eggs with spinach and pita"></span><div><small>Morning · 480 kcal</small>Scrambled Eggs with Spinach, Feta &amp; Pita</div><span class="edit"></span></div>
  <div class="meal"><span class="ph" role="img" aria-label="Black bean salad"></span><div><small>Afternoon · 350 kcal</small>No-Cook Black Bean Salad</div><span class="edit"></span></div>
  <div class="meal"><span class="ph" role="img" aria-label="Glazed salmon with garlic"></span><div><small>Evening · 390 kcal</small>Gochujang-Glazed Salmon with Garlic</div><span class="edit"></span></div>
  <div class="nav"><i></i><i class="on"></i><i></i><i></i><i></i></div>
</div>
<div class="note" style="left:522px;top:996px">Premium user can add their diet plan</div>
<div class="note" style="left:522px;top:1018px">They can change their food also, using this edit icon</div>

</body>
</html>
```